Business Card/Letterhead/Envelope design
KTL & Associates
Business Card/Letterhead/Envelope design -
Creative Brief
Professional
Gregory P. Holt
Principal
2947 Brambleton Way Suite 340 Frisco, Texas 75981
gregory@ktlva.com
www.ktlva.com
Rounded corners preferable Simple Clean Cutting Edge Front: Full Color on White background or Full Color on Black background Back: Full Color on Black background
Reversed Logo centered on the back of card w/slogan of company... Passion. Performance. Results. (Black background)

```html
<!DOCTYPE html>
<html lang="en">
<head>
<meta charset="utf-8">
<title>KTL &amp; Associates — Business Card</title>
<link rel="stylesheet" href="https://fonts.googleapis.com/css2?family=Arimo:ital,wght@0,400;0,700;1,400;1,700&display=swap">
<style>
  :root {
    --page: #e9e6e2;
    --card: #ffffff;
    --red: #d81e1e;
    --red-deep: #a80f12;
    --charcoal: #2b2b2b;
    --swoosh-grey: #9a9a9a;
    --ink-light: #ffffff;
  }
  html, body {
    margin: 0;
    width: 1200px;
    height: 780px;
    overflow: hidden;
    background: var(--page);
    font-family: "Arimo", Arial, sans-serif;
  }
  .business-card {
    position: absolute;
    left: 110px;
    top: 115px;
    width: 980px;
    height: 550px;
    border-radius: 44px;
    background: var(--card);
    overflow: hidden;
    box-shadow: 0 10px 30px rgba(0,0,0,0.18);
  }
  .card-band {
    position: absolute;
    inset: 0;
    width: 100%;
    height: 100%;
  }
  .brand {
    position: absolute;
    left: 200px;
    top: 62px;
  }
  .brand-name {
    margin: 0;
    font-size: 64px;
    font-weight: 700;
    color: var(--red);
    letter-spacing: 1px;
    line-height: 1;
  }
  .brand-tagline {
    margin: 12px 0 0 4px;
    font-size: 27px;
    color: var(--charcoal);
  }
  .person {
    position: absolute;
    right: 540px;
    top: 360px;
    text-align: right;
    color: var(--ink-light);
  }
  .person-name {
    margin: 0;
    font-size: 26px;
    font-weight: 700;
    font-style: italic;
  }
  .person-title {
    margin: 6px 0 30px;
    font-size: 19px;
    font-weight: 700;
    font-style: italic;
  }
  .person-address {
    margin: 0;
    font-size: 18px;
    line-height: 1.4;
    font-style: normal;
  }
  .divider {
    position: absolute;
    left: 470px;
    top: 330px;
    width: 2px;
    height: 168px;
    background: var(--ink-light);
  }
  .contacts {
    position: absolute;
    left: 490px;
    top: 322px;
    margin: 0;
    padding: 0;
    list-style: none;
    color: var(--ink-light);
    font-size: 18px;
  }
  .contacts li {
    display: flex;
    align-items: center;
    height: 30px;
  }
  .contacts svg {
    width: 18px;
    height: 18px;
    margin-right: 14px;
    fill: var(--ink-light);
    flex: none;
  }
</style>
</head>
<body>
  <div class="business-card">
    <svg class="card-band" viewBox="0 0 980 550" preserveAspectRatio="none" aria-hidden="true">
      <defs>
        <linearGradient id="bandRed" x1="0" y1="0" x2="0" y2="1">
          <stop offset="0" stop-color="#e8262a"/>
          <stop offset="1" stop-color="#b8121a"/>
        </linearGradient>
      </defs>
      <path d="M0 262 C 240 330, 520 300, 980 186 L980 220 C 560 330, 260 360, 0 296 Z" fill="var(--swoosh-grey)"/>
      <path d="M0 282 C 250 350, 540 318, 980 206 L980 236 C 560 342, 260 372, 0 312 Z" fill="var(--charcoal)"/>
      <path d="M0 304 C 260 370, 560 338, 980 228 L980 550 L0 550 Z" fill="url(#bandRed)"/>
    </svg>

    <div class="brand">
      <p class="brand-name">KTL &amp; Associates</p>
      <p class="brand-tagline">Business Sales/Mergers &amp; Acquisitions</p>
    </div>

    <div class="person">
      <p class="person-name">Gregory P. Holt</p>
      <p class="person-title">Principal</p>
      <address class="person-address">2947 Brambleton Way, Suite 340<br>Frisco, Texas 75981</address>
    </div>

    <div class="divider"></div>

    <ul class="contacts">
      <li><svg viewBox="0 0 24 24"><path d="M6 2h4l2 5-3 2a12 12 0 0 0 6 6l2-3 5 2v4a2 2 0 0 1-2 2A18 18 0 0 1 4 4a2 2 0 0 1 2-2z"/></svg>555.210.4863</li>
      <li><svg viewBox="0 0 24 24"><path d="M7 1h10a2 2 0 0 1 2 2v18a2 2 0 0 1-2 2H7a2 2 0 0 1-2-2V3a2 2 0 0 1 2-2zm0 3v14h10V4z"/></svg>555.318.2097</li>
      <li><svg viewBox="0 0 24 24"><path d="M6 2h10v6H6zM3 9h18v10h-3v3H6v-3H3zm5 6v5h8v-5z"/></svg>555.746.1352</li>
      <li><svg viewBox="0 0 24 24"><path d="M12 2a10 10 0 1 0 6 18l-1-2a8 8 0 1 1 5-6c0 2-1 3-2 3s-2-1-2-2V7h-2v1a5 5 0 1 0 1 7c1 2 2 2 3 2 3 0 4-3 4-5A10 10 0 0 0 12 2zm0 13a3 3 0 1 1 0-6 3 3 0 0 1 0 6z"/></svg>gregory@ktlva.com</li>
      <li><svg viewBox="0 0 24 24"><path d="M12 2a10 10 0 1 0 0 20 10 10 0 0 0 0-20zm7.9 9h-3.9a15 15 0 0 0-1.4-6.5A8 8 0 0 1 19.9 11zM12 4c1 1.3 1.9 3.8 2 7h-4c.1-3.2 1-5.7 2-7zM9.4 4.5A15 15 0 0 0 8 11H4.1a8 8 0 0 1 5.3-6.5zM4.1 13H8a15 15 0 0 0 1.4 6.5A8 8 0 0 1 4.1 13zM12 20c-1-1.3-1.9-3.8-2-7h4c-.1 3.2-1 5.7-2 7zm2.6-.5A15 15 0 0 0 16 13h3.9a8 8 0 0 1-5.3 6.5z"/></svg>www.ktlva.com</li>
    </ul>
  </div>
</body>
</html>
```